High-end construction company needs a business card design

We need a modern looking business card that draws people in, is memorable and looks so good people will want to sick it on their fridges.
On the first side what is needed are:
Logo
My name - Tomas Brevik
Title - Managing Director
Website - www.kelvora.co.uk
Email - tomas@kelvora.co.uk
Telephone - 020 4917 2365
Mobile - 07845139072
On the back side was is needed is a list of all the services we provide:
-Kitchen Renovations
-Bathroom Renovations
-House Renovations
-Garage Conversions
-Extensions
-Loft Conversions
-Conservatories
-Carpentry
-Tiling
-Electrical
-Plumbing & Heating
-Bricklaying
-Landscaping
-Decorating
-Plastering
We would like the colours to be the same shades as on the logo with grey or black for the words.
Target Market(s)
Anyone who needs building work done
Contact Information for Business Card
This business card is for a construction company which strives to deliver excellent service and quality.
The look and feel of the card should represent this.
Requirements
Must have
- On the first side what is needed are:
Logo
My name - Tomas Brevik
Title - Managing Director
Website - www.kelvora.co.uk
Email - tomas@kelvora.co.uk
Telephone - 020 4917 2365
Mobile - 07845139072
Nice to have
- Cool looking features

```html
<!DOCTYPE html>
<html lang="en">
<head>
<meta charset="utf-8">
<title>Kelvora Construction Ltd – Business Card</title>
<link href="https://fonts.googleapis.com/css2?family=Open+Sans:wght@400;600;700;800&display=swap" rel="stylesheet">
<style>
  :root {
    --green: #5fb83a;
    --green-bright: #6cc940;
    --black: #1d1d1d;
    --charcoal: #2a2a2a;
    --ink: #222222;
    --stage: #e6e8ea;
  }
  * { margin: 0; padding: 0; box-sizing: border-box; }
  html, body { width: 1200px; height: 900px; overflow: hidden; }
  body {
    background: var(--stage);
    font-family: "Open Sans", Arial, sans-serif;
    display: flex;
    align-items: center;
    justify-content: center;
    gap: 40px;
  }
  .card {
    position: relative;
    width: 540px;
    height: 350px;
    overflow: hidden;
    border-radius: 4px;
    box-shadow: 0 12px 30px rgba(0,0,0,.18);
  }

  /* Back side – services */
  .card--services { background: var(--green); color: var(--ink); }
  .services__band {
    position: absolute; left: 0; right: 0; top: 22px; height: 26px;
    background: var(--charcoal);
  }
  .services__title {
    position: absolute; left: 0; right: 0; top: 56px;
    text-align: center; font-weight: 700; font-size: 21px; letter-spacing: .5px;
    color: var(--charcoal);
  }
  .services__col {
    position: absolute; list-style: none; font-size: 14px; line-height: 27px;
  }
  .services__col li::before {
    content: ""; display: inline-block; width: 6px; height: 6px; border-radius: 50%;
    background: var(--ink); margin-right: 10px; vertical-align: middle;
  }
  .services__col--one { left: 34px; top: 100px; }
  .services__col--two { left: 218px; top: 127px; }
  .services__col--three { left: 380px; top: 154px; }
  .services__brand {
    position: absolute; right: 30px; bottom: 26px;
    display: flex; align-items: center; gap: 8px;
    font-weight: 800; font-size: 26px; color: var(--charcoal); letter-spacing: 1px;
  }
  .services__brand .mark { width: 16px; height: 16px; background: var(--charcoal); }

  /* Front side – contact */
  .card--contact { background: linear-gradient(160deg, #2b2b2b, var(--black) 70%); color: var(--green); }
  .contact__stripe { position: absolute; inset: 0; }
  .contact__brand {
    position: absolute; left: 66px; top: 46px;
    display: flex; align-items: center; gap: 10px;
    font-weight: 800; font-size: 34px; letter-spacing: 1px; color: var(--green);
  }
  .contact__brand .mark { width: 18px; height: 18px; background: var(--green); }
  .contact__name {
    position: absolute; left: 66px; top: 108px;
    font-weight: 700; font-size: 25px; color: var(--green);
  }
  .contact__role {
    position: absolute; left: 66px; top: 142px;
    font-size: 15px; color: var(--green); opacity: .85;
  }
  .contact__list {
    position: absolute; right: 34px; top: 232px; list-style: none;
    text-align: right; font-weight: 600; font-size: 15px; line-height: 24px; color: var(--green-bright);
  }
</style>
</head>
<body>

<section class="card card--services" aria-label="Services side">
  <div class="services__band"></div>
  <h2 class="services__title">List of Our Services</h2>
  <ul class="services__col services__col--one">
    <li>Kitchen Renovations</li>
    <li>Bathroom Renovations</li>
    <li>House Renovations</li>
    <li>Garage Conversions</li>
    <li>Extensions</li>
    <li>Plastering</li>
  </ul>
  <ul class="services__col services__col--two">
    <li>Loft Conversions</li>
    <li>Conservatories</li>
    <li>Carpentry</li>
    <li>Tiling</li>
    <li>Electrical</li>
    <li>Decorating</li>
  </ul>
  <ul class="services__col services__col--three">
    <li>Landscaping</li>
    <li>Bricklaying</li>
    <li>Plumbing &amp; Heating</li>
  </ul>
  <div class="services__brand"><span class="mark"></span>KELVORA</div>
</section>

<section class="card card--contact" aria-label="Contact side">
  <svg class="contact__stripe" width="540" height="350" viewBox="0 0 540 350" aria-hidden="true">
    <polygon points="0,218 540,150 540,178 0,248" fill="#6cc940"/>
    <g fill="none" stroke="#1d1d1d" stroke-width="1.6">
      <!-- globe -->
      <circle cx="236" cy="205" r="7"/>
      <line x1="229" y1="205" x2="243" y2="205"/>
      <ellipse cx="236" cy="205" rx="3" ry="7"/>
      <!-- mail -->
      <rect x="265" y="194" width="15" height="10"/>
      <polyline points="265,194 272.5,200 280,194"/>
      <!-- phone -->
      <path d="M303 186 q-4 6 1 12 q5 5 10 2 l-3 -4 q-3 2 -5 -1 q-2 -3 1 -5 z" fill="#1d1d1d" stroke="none"/>
      <!-- mobile -->
      <rect x="334" y="176" width="9" height="16" rx="2"/>
      <line x1="337" y1="189" x2="340" y2="189"/>
    </g>
  </svg>
  <div class="contact__brand"><span class="mark"></span>KELVORA</div>
  <h1 class="contact__name">Tomas Brevik</h1>
  <p class="contact__role">Managing Director</p>
  <ul class="contact__list">
    <li>07845139072</li>
    <li>020 4917 2365</li>
    <li>tomas@kelvora.co.uk</li>
    <li>www.kelvora.co.uk</li>
  </ul>
</section>

</body>
</html>
```